Nobody Left the Lantern Burning - Tom Halvery - CD Cover Design Project

Single Cover for CD & Online media e.g. Tunebox Graphics
The first song release from Tom Halvery will be the track 'Nobody Left the Lantern Burning'.
For the release the single requires artwork that is eye catching, seriously professional & meets the requirements of Disc Sprout, Tunebox and also a physical copy on CD.
Track listings for CD will be:
1. Nobody Left the Lantern Burning
2. Nobody Left the Lantern Burning - Instrumental
see details in this link:
http://members.discsprout-example.com/faq.aspx
http://selfmadesound.discsprout-example.com/2009/11/avoid-album-art-atrocities/
http://answers.quorvex-example.com/question/index?qid=20111015141433AAdDTmH
Any advice on this would be greatly appreciated,
I would also like the two logo's I have uploaded to be used,
one is the Tom Halvery logo and the other is for Milbrook & Tandy Records logo (please remove the R and replace with a C for copyright.)
There are four high res photo shopped pictures of Tom Halvery and another zip file of many others, it would be nice to include one of these maybe on the 2nd page or back of the CD. Please don't use them as the front cover.
I imagine an Art Deco illustration but please listen to the track and let it inspire you.
Good Luck
Updates
I don't feel this is what I'm looking for, the design needs to refelct a broken heart without being a picture of a broken heart
Reason: No design has been what we are after so far so the deadline has been extended and the budget increased.

```html
<!DOCTYPE html>
<html lang="en">
<head>
<meta charset="utf-8">
<title>Tom Halvery – Nobody Left the Lantern Burning</title>
<link href="https://fonts.googleapis.com/css2?family=Raleway:wght@300;400&family=Pinyon+Script&family=Oswald:wght@400&display=swap" rel="stylesheet">
<style>
  :root {
    --cream: #fff3de;
    --peach: #f2b48e;
    --rose: #d96a78;
    --plum: #5a2550;
    --night: #2c1636;
    --band: #c0304f;
    --band-text: #f6c9d2;
    --ink: #3a2228;
    --title-grey: rgba(120, 110, 120, 0.35);
  }
  html, body {
    margin: 0;
    padding: 0;
    width: 1200px;
    height: 1200px;
    overflow: hidden;
    background: #ffffff;
  }
  .cover {
    position: relative;
    width: 1200px;
    height: 1200px;
    overflow: hidden;
    font-family: "Raleway", sans-serif;
  }
  .cover-photo {
    position: absolute;
    left: 0;
    top: 0;
    width: 1200px;
    height: 1058px;
    background:
      radial-gradient(ellipse 520px 460px at 170px 170px, var(--cream) 0%, rgba(255,236,214,0.85) 35%, rgba(242,180,142,0) 75%),
      radial-gradient(ellipse 520px 620px at 900px 620px, rgba(232,132,110,0.9) 0%, rgba(217,106,120,0.6) 45%, rgba(217,106,120,0) 80%),
      linear-gradient(160deg, var(--peach) 0%, var(--rose) 45%, var(--plum) 78%, var(--night) 100%);
  }
  .track-list {
    position: absolute;
    left: 90px;
    top: 322px;
    font-weight: 300;
    font-size: 24px;
    line-height: 30.5px;
    color: var(--ink);
    letter-spacing: 0.3px;
  }
  .track-list p { margin: 0; }
  .release-title {
    position: absolute;
    left: 212px;
    top: 748px;
    width: 760px;
    display: flex;
    justify-content: space-between;
    font-family: "Oswald", sans-serif;
    font-size: 62px;
    line-height: 1;
    color: var(--title-grey);
  }
  .artist-name {
    position: absolute;
    left: 96px;
    top: 838px;
    margin: 0;
    font-family: "Pinyon Script", cursive;
    font-weight: 400;
    font-size: 100px;
    line-height: 1.2;
    color: var(--cream);
  }
  .label-band {
    position: absolute;
    left: 0;
    top: 1058px;
    width: 1200px;
    height: 142px;
    background: var(--band);
  }
  .copyright {
    position: absolute;
    left: 45px;
    top: 67px;
    font-size: 15px;
    font-weight: 300;
    color: var(--band-text);
    letter-spacing: 0.3px;
  }
  .artist-mark {
    position: absolute;
    left: 930px;
    top: 84px;
    width: 70px;
    font-size: 13px;
    font-weight: 400;
    line-height: 1.15;
    color: var(--ink);
    text-align: center;
  }
  .label-mark {
    position: absolute;
    left: 1022px;
    top: 36px;
    width: 148px;
    font-size: 13px;
    font-weight: 400;
    line-height: 1.25;
    color: var(--ink);
    text-align: center;
  }
  .label-mark .dot {
    display: block;
    width: 40px;
    height: 40px;
    margin: 0 auto 10px;
    border-radius: 50%;
    background: var(--ink);
  }
</style>
</head>
<body>
<main class="cover">
  <div class="cover-photo" role="img" aria-label="Warm soft-focus portrait of the artist in glasses holding a pen, with glowing pink and cream bokeh lights"></div>

  <div class="track-list">
    <p>Track:</p>
    <p>1. Nobody Left the Lantern Burning</p>
    <p>2. Nobody Left the Lantern Burning - Instrumental</p>
  </div>

  <div class="release-title" aria-label="Noctella">
    <span>N</span><span>O</span><span>C</span><span>T</span><span>E</span><span>L</span><span>L</span><span>A</span>
  </div>

  <h1 class="artist-name">Tom Halvery</h1>

  <footer class="label-band">
    <div class="copyright">©2012.MILBROOK&amp;TANDYRECORDS</div>
    <div class="artist-mark">TOM<br>HALVERY</div>
    <div class="label-mark"><span class="dot"></span>MILBROOK &amp; TANDY<br>RECORDS</div>
  </footer>
</main>
</body>
</html>
```